Harbor Ridge Labs and VELARA

I'd like to create an announcement which will be posted on our website (www.harborridgelabs.example) that announces our partnership with VELARA, a large Dominican community healthcare service in the greater NYC area. Harbor Ridge Labs (my company) is one of two medical laboratories that are considered "preferred laboratories" for VELARA. I will include an example of what the other preferred laboratory (Trulane laboratory) has on their website.
My website - www.harborridgelabs.example
Velara preferred listings - https://velaracarenet.example/wp-content/uploads/2020/09/5-VELARA-Tier-2-Network-2020-09.pdf
Example of how we helped VELARA clients and the Dominican consulate - https://playamarinoticias.example/consulado-rd-ny-concluye-vuelos-ferry-para-dominicanos-varados-en-ee-uu-por-covid-19/
Trulane announcement on their website - https://www.trulane.example/trulane-laboratories-forms-a-strategic-collaboration-with-velara-to-improve-health-outcomes-of-underserved-new-yorkers/

```html
<!DOCTYPE html>
<html lang="en">
<head>
<meta charset="utf-8">
<title>Harbor Ridge Laboratories – VELARA Partnership Announcement</title>
<link href="https://fonts.googleapis.com/css2?family=Montserrat:wght@400;500;600;700&family=Roboto:wght@400;500;700&family=Rajdhani:wght@500;600&display=swap" rel="stylesheet">
<style>
:root{
  --red:#cc0000;
  --navy:#22207a;
  --navy-deep:#1b1a63;
  --green:#3a8f7c;
  --green-btn:#3d9a7f;
  --ink:#3d3d3d;
  --muted:#6b6b6b;
  --line:#d9d9d9;
  --white:#ffffff;
  --canvas:#ffffff;
}
*{box-sizing:border-box;margin:0;padding:0}
html,body{width:1200px;height:702px;overflow:hidden;background:var(--canvas)}
body{position:relative;font-family:"Montserrat",sans-serif;color:var(--ink)}

.page{position:absolute;top:35px;width:560px;height:614px;background:var(--white);overflow:hidden;box-shadow:0 0 4px rgba(0,0,0,.12)}
.page--home{left:28px}
.page--popup{left:613px}

.alert-bar{position:absolute;left:0;top:0;width:100%;height:17px;background:var(--red);color:var(--white);font:700 5.3px/17px "Roboto",sans-serif}
.alert-bar__text{position:absolute;left:160px}
.alert-bar__btn{position:absolute;left:372px;top:3.5px;width:30px;height:10px;border:.6px solid var(--white);border-radius:2px;font-size:4px;line-height:9px;text-align:center}

.brand{position:absolute;display:flex;align-items:center;gap:3px;color:var(--green);font-weight:700;white-space:nowrap}
.brand__dot{display:block;border-radius:50%;background:var(--navy)}
.brand--header{left:56px;top:32px;font-size:7.4px}
.brand--header .brand__dot{width:9px;height:9px}

.contact{position:absolute;top:28px;display:flex;gap:4px;font-family:"Roboto",sans-serif}
.contact svg{width:9px;height:9px;margin-top:1px}
.contact__label{font-size:5.3px;font-weight:700;color:var(--navy)}
.contact__value{font-size:3.8px;color:var(--muted);margin-top:1px}
.contact--phone{left:241px}
.contact--email{left:332px}
.contact--hq{left:414px}

.hero{position:absolute;left:0;top:60px;width:100%;height:130px;background:linear-gradient(100deg,#2c4a66 0%,#4a6c88 35%,#b8c3cf 60%,#d9c4b8 75%,#6e8196 100%)}
.hero__shade{position:absolute;inset:0;background:linear-gradient(90deg,rgba(20,35,60,.55),rgba(20,35,60,.1) 70%)}
.hero__title{position:absolute;left:60px;top:28px;color:var(--white);font-weight:700;font-size:18.5px;line-height:18.5px}
.hero__sub{position:absolute;left:60px;top:72px;color:var(--white);font-size:6.2px}
.hero__btn{position:absolute;top:84px;height:15.5px;background:var(--green-btn);color:var(--white);font:500 5.2px/15.5px "Roboto",sans-serif;text-align:center;border-radius:1.5px}

.main-nav{position:absolute;left:52px;top:51px;width:456px;height:19px;background:var(--navy);border-top:1px solid var(--green);font:500 4.6px/18px "Roboto",sans-serif;color:var(--white)}
.main-nav__item{position:absolute;top:0}
.main-nav__item--caret::after{content:" \25BE"}
.main-nav__btn{position:absolute;top:4px;height:11px;line-height:11px;background:var(--green-btn);text-align:center;border-radius:1px}

.intro{position:absolute;left:0;top:218px;width:100%;text-align:center}
.intro__title{font-size:14.2px;font-weight:600;color:#404040}
.intro__title em{font-style:normal;color:var(--green)}
.intro__rule{width:32px;height:1px;background:var(--green);margin:6px auto 0}
.intro__text{width:364px;margin:6px auto 0;font-size:6.1px;line-height:9px;color:var(--muted)}

.card{position:absolute;top:290px;width:164px;height:154px;background:var(--white);box-shadow:0 0 3px rgba(0,0,0,.12);text-align:center}
.card--genetic{left:109.5px}
.card--available{left:290px}
.card__media{width:100%;height:86px}
.card--genetic .card__media{background:linear-gradient(135deg,#dfe6ee,#9fb1c6 55%,#4a5f86)}
.card--available .card__media{background:linear-gradient(135deg,#e8e8e6,#b9b8b3 50%,#6f716f)}
.card__kicker{margin-top:6px;font-size:10px;color:#555;line-height:10px}
.card__title{font-size:17px;font-weight:700;color:var(--green);line-height:17px}
.card__text{width:156px;margin:7px auto 0;font-size:4.7px;line-height:7.3px;color:var(--muted)}

.footer-rule{position:absolute;left:52px;width:456px;height:1px;background:var(--line)}
.footer-rule--top{top:487px;height:1.2px;background:var(--green)}
.footer-rule--mid{top:568px}
.footer-rule--bot{top:587px}
.brand--footer{left:61px;top:506px;font-size:6.5px}
.brand--footer .brand__dot{width:8px;height:8px}
.footer-about{position:absolute;left:60px;top:536px;font-size:4.3px;line-height:8px;color:var(--muted)}
.newsletter__label{position:absolute;left:290px;top:512px;font:500 5.8px "Roboto",sans-serif;color:var(--navy)}
.newsletter__input{position:absolute;top:525.5px;width:69px;height:12.5px;border:.6px solid var(--line);font-size:3.8px;line-height:11.5px;padding-left:5px;color:#999}
.newsletter__btn{position:absolute;left:434.5px;top:525.5px;width:69px;height:12.5px;background:var(--green-btn);color:var(--white);font:700 3.8px/12.5px "Montserrat",sans-serif;letter-spacing:1.6px;text-align:center}
.copyright{position:absolute;left:0;width:560px;top:596px;text-align:center;font-size:3.8px;color:var(--muted)}

.overlay{position:absolute;inset:0;background:rgba(0,0,0,.62)}
.modal{position:absolute;left:70.5px;top:85px;width:418.5px;height:373px;background:var(--white);text-align:center;font-family:"Rajdhani",sans-serif}
.modal__close{position:absolute;left:476.5px;top:75.5px;width:25px;height:25px;border-radius:50%;background:#111;border:1.5px solid var(--white)}
.modal__close svg{position:absolute;left:7.5px;top:7.5px;width:7px;height:7px}
.brand--modal{left:156px;top:108px;font-size:10px;font-family:"Montserrat",sans-serif}
.brand--modal .brand__dot{width:12px;height:12px}
.modal__media{position:absolute;left:24.5px;top:67px;width:370px;height:155.5px;background:linear-gradient(120deg,#f0f4f8,#b8c9db 40%,#6e8db0 70%,#dfe7ef)}
.modal__message{position:absolute;left:0;top:236px;width:100%;font-weight:600;font-size:9px;line-height:16px;color:var(--navy);letter-spacing:.2px}
.modal__input{position:absolute;left:39.5px;top:279px;width:339px;height:27px;border:.7px solid #cfcfcf;border-radius:14px;text-align:left;padding-left:11px;font-size:7.4px;line-height:26px;color:#555}
.modal__btn{position:absolute;left:162.5px;top:314px;width:94px;height:26.5px;border-radius:14px;background:linear-gradient(90deg,var(--green),var(--navy));color:var(--white);font-weight:600;font-size:7.4px;line-height:26.5px;letter-spacing:.3px}
</style>
</head>
<body>

<section class="page page--home" aria-label="Harbor Ridge Laboratories homepage">
  <div class="alert-bar"><span class="alert-bar__text">Coronavirus Disease 2019 (COVID-19) Total COVID-19 Tests Performed - 654,249</span><span class="alert-bar__btn">Read More</span></div>
  <div class="brand brand--header"><span class="brand__dot"></span>Harbor Ridge Labs</div>
  <div class="contact contact--phone"><svg viewBox="0 0 24 24"><path d="M6.6 10.8a15 15 0 0 0 6.6 6.6l2.2-2.2a1 1 0 0 1 1-.25 11.4 11.4 0 0 0 3.6.57 1 1 0 0 1 1 1V20a1 1 0 0 1-1 1A17 17 0 0 1 3 4a1 1 0 0 1 1-1h3.5a1 1 0 0 1 1 1c0 1.25.2 2.45.57 3.57a1 1 0 0 1-.25 1z" fill="#a9a9a9"/></svg><div><div class="contact__label">Telephone</div><div class="contact__value">800-555-0142 (800-555-0142)</div></div></div>
  <div class="contact contact--email"><svg viewBox="0 0 24 24"><rect x="3" y="5" width="18" height="14" rx="1" fill="none" stroke="#a9a9a9" stroke-width="1.8"/><path d="M3 6l9 7 9-7" fill="none" stroke="#a9a9a9" stroke-width="1.8"/></svg><div><div class="contact__label">Email Address</div><div class="contact__value">info@harborridgelabs.example</div></div></div>
  <div class="contact contact--hq"><svg viewBox="0 0 24 24"><path d="M12 2a7 7 0 0 0-7 7c0 5 7 13 7 13s7-8 7-13a7 7 0 0 0-7-7zm0 9.5A2.5 2.5 0 1 1 12 6.5a2.5 2.5 0 0 1 0 5z" fill="#a9a9a9"/></svg><div><div class="contact__label">Corporate Headquarters</div><div class="contact__value">118 Tidewater Ave Brooklyn NY 11200</div></div></div>

  <div class="hero">
    <div role="img" aria-label="Photo of a scientist in safety goggles at a microscope in a laboratory" style="position:absolute;inset:0"></div>
    <div class="hero__shade"></div>
    <h1 class="hero__title">The World's Leading<br>Diagnostics Laboratory</h1>
    <p class="hero__sub">Interested in signing up with Harbor Ridge Laboratories – click here</p>
    <span class="hero__btn" style="left:67.6px;width:64.4px">CLINIX Access</span>
    <span class="hero__btn" style="left:158.5px;width:53.5px">Patient Portal</span>
    <span class="hero__btn" style="left:250px;width:51px">Pay your Bill</span>
  </div>

  <nav class="main-nav">
    <span class="main-nav__item" style="left:6px">About Us</span>
    <span class="main-nav__item main-nav__item--caret" style="left:36px">Patient Services</span>
    <span class="main-nav__item main-nav__item--caret" style="left:86px">Healthcare Providers</span>
    <span class="main-nav__item" style="left:145.5px">Test Directory</span>
    <span class="main-nav__item" style="left:184px">HIPAA</span>
    <span class="main-nav__item" style="left:209px">Careers</span>
    <span class="main-nav__item" style="left:236px">Contact Us</span>
    <span class="main-nav__item" style="left:269.5px">COVID-19</span>
    <span class="main-nav__btn" style="left:335.5px;width:28px">Sign Up</span>
    <span class="main-nav__btn" style="left:382px;width:67px">Book Appointment Online</span>
  </nav>

  <div class="intro">
    <h2 class="intro__title">Tests designed for <em>Your Convenience.</em></h2>
    <div class="intro__rule"></div>
    <p class="intro__text">Harbor Ridge Laboratories is pleased to offer its services to you and your patients. You can use our webpage to learn about the services we provide from the comfort of your own home. Harbor Ridge Laboratories provides numerous patient services with convenient hours. Our secure electronic health records guarantee confidential information for you and your patients by increasing lab productivity and providing you with the support and information that you need.</p>
  </div>

  <article class="card card--genetic">
    <div class="card__media" role="img" aria-label="Photo of lab technicians working at microscopes"></div>
    <div class="card__kicker">Integrated Genetic</div>
    <div class="card__title">Solutions</div>
    <p class="card__text">IGS provides a comprehensive and fully customized solution to help you reach your ideal mental and physical potential.</p>
  </article>
  <article class="card card--available">
    <div class="card__media" role="img" aria-label="Photo of gloved hands loading a sample tube into a centrifuge"></div>
    <div class="card__kicker">Always Available</div>
    <div class="card__title">For You</div>
    <p class="card__text">We're there for you 24/7. Click here to ask anything about our methods and equipment.</p>
  </article>

  <div class="footer-rule footer-rule--top"></div>
  <div class="brand brand--footer"><span class="brand__dot"></span>Harbor Ridge Labs</div>
  <p class="footer-about">Harbor Ridge Laboratories is dedicated to<br>providing superior service to your medical practice.</p>
  <div class="newsletter__label">Subscribe to our Newsletter</div>
  <div class="newsletter__input" style="left:290px">Your Name</div>
  <div class="newsletter__input" style="left:362px">Your Email</div>
  <div class="newsletter__btn">SUBSCRIBE</div>
  <div class="footer-rule footer-rule--mid"></div>
  <div class="footer-rule footer-rule--bot"></div>
  <p class="copyright">© 2020 Harbor Ridge Laboratories, Inc. All Rights Reserved. HRL and Harbor Ridge Laboratories are registered trademarks of Harbor Ridge Laboratories®, Inc.</p>
</section>

<section class="page page--popup" aria-label="Homepage with VELARA partnership announcement">
  <div aria-hidden="true">
    <div class="alert-bar"><span class="alert-bar__text">Coronavirus Disease 2019 (COVID-19) Total COVID-19 Tests Performed - 654,249</span><span class="alert-bar__btn">Read More</span></div>
    <div class="brand brand--header"><span class="brand__dot"></span>Harbor Ridge Labs</div>
    <div class="contact contact--phone"><svg viewBox="0 0 24 24"><path d="M6.6 10.8a15 15 0 0 0 6.6 6.6l2.2-2.2a1 1 0 0 1 1-.25 11.4 11.4 0 0 0 3.6.57 1 1 0 0 1 1 1V20a1 1 0 0 1-1 1A17 17 0 0 1 3 4a1 1 0 0 1 1-1h3.5a1 1 0 0 1 1 1c0 1.25.2 2.45.57 3.57a1 1 0 0 1-.25 1z" fill="#a9a9a9"/></svg><div><div class="contact__label">Telephone</div><div class="contact__value">800-555-0142 (800-555-0142)</div></div></div>
    <div class="contact contact--email"><svg viewBox="0 0 24 24"><rect x="3" y="5" width="18" height="14" rx="1" fill="none" stroke="#a9a9a9" stroke-width="1.8"/><path d="M3 6l9 7 9-7" fill="none" stroke="#a9a9a9" stroke-width="1.8"/></svg><div><div class="contact__label">Email Address</div><div class="contact__value">info@harborridgelabs.example</div></div></div>
    <div class="contact contact--hq"><svg viewBox="0 0 24 24"><path d="M12 2a7 7 0 0 0-7 7c0 5 7 13 7 13s7-8 7-13a7 7 0 0 0-7-7zm0 9.5A2.5 2.5 0 1 1 12 6.5a2.5 2.5 0 0 1 0 5z" fill="#a9a9a9"/></svg><div><div class="contact__label">Corporate Headquarters</div><div class="contact__value">118 Tidewater Ave Brooklyn NY 11200</div></div></div>
    <div class="hero">
      <div class="hero__shade"></div>
      <div class="hero__title">The World's Leading<br>Diagnostics Laboratory</div>
      <div class="hero__sub">Interested in signing up with Harbor Ridge Laboratories – click here</div>
    </div>
    <div class="main-nav">
      <span class="main-nav__item" style="left:6px">About Us</span>
      <span class="main-nav__item main-nav__item--caret" style="left:36px">Patient Services</span>
      <span class="main-nav__item main-nav__item--caret" style="left:86px">Healthcare Providers</span>
      <span class="main-nav__item" style="left:145.5px">Test Directory</span>
      <span class="main-nav__item" style="left:184px">HIPAA</span>
      <span class="main-nav__item" style="left:209px">Careers</span>
      <span class="main-nav__item" style="left:236px">Contact Us</span>
      <span class="main-nav__item" style="left:269.5px">COVID-19</span>
      <span class="main-nav__btn" style="left:335.5px;width:28px">Sign Up</span>
      <span class="main-nav__btn" style="left:382px;width:67px">Book Appointment Online</span>
    </div>
    <div class="footer-rule footer-rule--top"></div>
    <div class="brand brand--footer"><span class="brand__dot"></span>Harbor Ridge Labs</div>
    <p class="footer-about">Harbor Ridge Laboratories is dedicated to<br>providing superior service to your medical practice.</p>
    <div class="newsletter__label">Subscribe to our Newsletter</div>
    <div class="newsletter__input" style="left:290px">Your Name</div>
    <div class="newsletter__input" style="left:362px">Your Email</div>
    <div class="newsletter__btn">SUBSCRIBE</div>
    <div class="footer-rule footer-rule--mid"></div>
    <div class="footer-rule footer-rule--bot"></div>
    <p class="copyright">© 2020 Harbor Ridge Laboratories, Inc. All Rights Reserved. HRL and Harbor Ridge Laboratories are registered trademarks of Harbor Ridge Laboratories®, Inc.</p>
  </div>

  <div class="overlay"></div>

  <div class="modal" role="dialog" aria-label="VELARA partnership announcement">
    <div class="modal__media" role="img" aria-label="Photo of a team of scientists working together at a lab bench"></div>
    <p class="modal__message">WE ARE &nbsp;PARTNERSHIP WITH VELARA, A LARGE DOMINICAN COMMUNITY<br>HEALTHCARE SERVICE IN THE GREATER NYC AREA</p>
    <div class="modal__input">Enter Your Email :</div>
    <div class="modal__btn">GO TO NEXT PAGE</div>
  </div>
  <div class="brand brand--modal"><span class="brand__dot"></span>Harbor Ridge Labs</div>
  <div class="modal__close" aria-label="Close"><svg viewBox="0 0 10 10"><path d="M1 1l8 8M9 1l-8 8" stroke="#fff" stroke-width="2.2" stroke-linecap="round"/></svg></div>
</section>

</body>
</html>
```